Ground breaking athletic gear company needs a kick ass business card

We are an American start up athletic gear company that uses a medically proven biohack to boost athletic performance. Heat kills strength and endurance. Our gear helps athletes manage heat better and ultimatley can improve them by up to 10% instantly. Nothing like it out there! Launching this summer.
We are looking for a modern, minimalist design that captures a sporty edge. Check out www.velmarunwear.com, @velmarunwear on instagram for more ideas.

Target Market(s)

25-35 year olds, male and female athletes, vaultlift athletes, competitive runners

Industry/Entity Type

Business

Contact Information for Business Card

Dorian Pellham
Founder
dorianp@velmarunwear.com
www.VelmaRunwear.com
+1 (555) 014-2286

Font styles to use
Sans Serif

Requirements
Must have
• Logo and icon
• All contact information
• dorianp@velmarunwear.com
• +1 (555) 019-4471 M
• +1 (555) 014-2286
Nice to have
• Tag line : "Chill & Prevail"

```html
<!DOCTYPE html>
<html lang="en">
<head>
<meta charset="UTF-8">
<title>Velma Runwear — Business Card</title>
<link rel="stylesheet" href="https://fonts.googleapis.com/css2?family=Open+Sans:wght@400;600;700&family=Quicksand:wght@500&display=swap">
<style>
  :root {
    --backdrop: #3a332f;
    --card-black: #1a1a1b;
    --card-edge: #262627;
    --ink-white: #f2f2f2;
    --ink-grey: #c9c9c9;
    --front-mark: #3b3b3c;
    --accent-blue: #6cb8ea;
  }
  * { margin: 0; padding: 0; box-sizing: border-box; }
  html, body {
    width: 1200px;
    height: 716px;
    overflow: hidden;
    background: var(--backdrop);
  }
  .canvas {
    position: relative;
    width: 1200px;
    height: 716px;
  }
  .card {
    position: absolute;
    top: 210px;
    width: 520px;
    height: 297px;
    background: var(--card-black);
    border: 1px solid var(--card-edge);
    border-radius: 4px;
    overflow: hidden;
    box-shadow: 0 12px 28px rgba(0,0,0,0.45);
  }
  .card--front { left: 50px; }
  .card--back { left: 630px; }

  /* Front */
  .front-mark {
    position: absolute;
    inset: 0;
    display: flex;
    align-items: center;
    justify-content: center;
    font-family: 'Open Sans', sans-serif;
    font-weight: 600;
    font-size: 26px;
    letter-spacing: 6px;
    color: var(--front-mark);
    text-transform: uppercase;
  }

  /* Back */
  .brand {
    position: absolute;
    top: 86px;
    right: 44px;
    display: flex;
    align-items: center;
    gap: 12px;
  }
  .brand__square {
    width: 14px;
    height: 14px;
    border: 1.5px solid var(--ink-white);
  }
  .brand__name {
    font-family: 'Open Sans', sans-serif;
    font-weight: 600;
    font-size: 20px;
    line-height: 1.15;
    letter-spacing: 4px;
    color: var(--ink-white);
    text-transform: uppercase;
  }
  .contact {
    position: absolute;
    top: 104px;
    left: 36px;
    font-family: 'Open Sans', sans-serif;
  }
  .contact__name {
    font-weight: 700;
    font-size: 17px;
    color: var(--accent-blue);
    line-height: 1.1;
  }
  .contact__title {
    font-size: 10px;
    color: var(--ink-grey);
    margin-top: 3px;
    margin-bottom: 14px;
  }
  .contact__list { list-style: none; }
  .contact__item {
    display: flex;
    align-items: center;
    gap: 9px;
    font-size: 11.5px;
    color: var(--ink-white);
    line-height: 19px;
  }
  .contact__icon { width: 10px; height: 10px; flex: none; }
  .tagline {
    position: absolute;
    right: 58px;
    bottom: 16px;
    font-family: 'Quicksand', sans-serif;
    font-weight: 500;
    font-size: 13px;
    letter-spacing: 2px;
    color: var(--ink-white);
    white-space: nowrap;
  }
  .corner-block {
    position: absolute;
    right: 0;
    bottom: 0;
    width: 34px;
    height: 22px;
    background: var(--accent-blue);
  }
</style>
</head>
<body>
<main class="canvas">
  <section class="card card--front" aria-label="Card front">
    <div class="front-mark">Velma Runwear</div>
  </section>

  <section class="card card--back" aria-label="Card back">
    <div class="brand">
      <span class="brand__square"></span>
      <span class="brand__name">Velma<br>Runwear</span>
    </div>

    <div class="contact">
      <p class="contact__name">Dorian Pellham</p>
      <p class="contact__title">Founder</p>
      <ul class="contact__list">
        <li class="contact__item">
          <svg class="contact__icon" viewBox="0 0 10 10" aria-hidden="true"><path d="M2 1 L4 1 L4.6 3 L3.4 4 Q4.3 5.8 6 6.6 L7 5.4 L9 6 L9 8 Q8.5 9 7.5 9 Q1 8 1 2.5 Q1 1.5 2 1 Z" fill="var(--accent-blue)"/></svg>
          +1 (555) 014-2286
        </li>
        <li class="contact__item">
          <svg class="contact__icon" viewBox="0 0 10 10" aria-hidden="true"><rect x="0.5" y="2" width="9" height="6.5" rx="0.8" fill="var(--accent-blue)"/><path d="M0.8 2.4 L5 5.6 L9.2 2.4" stroke="var(--card-black)" stroke-width="0.9" fill="none"/></svg>
          dorianp@velmarunwear.com
        </li>
        <li class="contact__item">
          <svg class="contact__icon" viewBox="0 0 10 10" aria-hidden="true"><circle cx="5" cy="5" r="4.4" fill="var(--accent-blue)"/><path d="M0.8 5 H9.2 M5 0.6 V9.4 M5 0.6 Q2.4 5 5 9.4 M5 0.6 Q7.6 5 5 9.4" stroke="var(--card-black)" stroke-width="0.7" fill="none"/></svg>
          www.VelmaRunwear.com
        </li>
      </ul>
    </div>

    <p class="tagline">Chill &amp; Prevail</p>
    <span class="corner-block"></span>
  </section>
</main>
</body>
</html>
```